Toy Company Needs a Web Site For a New Toy

We need a web site for a new toy called "Zippa Loop Trike". The bike is a plastic, non motorized ride on toy for kids ages 1.5 - 5 years of age. The bike is being launched in three colors, red, blue and pink, though we may include a black option too.

For the web site we want something bold and colorful that communicates fun, therefore NO dull colors like black or grey. Nothing too cluttered. We want the site to attract the attention of kids but also give the parents a sense of confidence in our professionalism as a trustworthy toy company. The home page should focus on the bike, with different views of the bike and a small write-up on some of its key features. We would also like the home page to have a video of the bike in play. A obvious link to the shopping basket must be present as well. The site must include a shopping basket and ordering system.

Attached is a screenshot of a site that has the colourfulness and playfulness that we are looking for. Please have a look.

The bike images attached are renderings from the CAD software, actual high res photos will be used when the site is developed.

The product logo is attached and MUST be used on the site. It must be BOLD and can be incorporated into the actual website design.

The site pages are:
Home
Gallery
Buy
Contact

Competitors:
www.brambleplay.example
www.quorvaride.example
I do not like either of their sites.

We only have one product at this time, so the site is to be focused on that product, not a whole catalog of products. It is really a single product with the ability to purchase.
Updates

Project Deadline Extended
Reason: I am extending this competition in order to give me more time to review each design and provide the feedback that the designers deserve.

Target Market(s)

Parents, children ages 1.5 - 5.

Industry/Entity Type

It Company

Colors
0555a3
eb1f27
9bcb3c
faed22
f78f20
f37022
e34197
a6459a
6b449b

Requirements
Must have
• Please use the logo attached, but feel free to use different colors.
Should not have
• Dull colors like black and grey

```html
<!DOCTYPE html>
<html lang="en">
<head>
<meta charset="utf-8">
<title>Zippa Loop Trike</title>
<link rel="stylesheet" href="https://fonts.googleapis.com/css2?family=Lilita+One&family=Alfa+Slab+One&family=Arimo:wght@400;700&display=swap">
<style>
  :root {
    --ink: #3b3d40;
    --sky-blue: #2fa3d8;
    --brand-red: #c9372c;
    --brand-red-dark: #8f2119;
    --gold: #e2a900;
    --gold-dark: #c48a00;
    --video-bg: #1f2022;
    --video-icon: #45464a;
    --footer-bg: #d6d6d6;
    --footer-line: #bdbdbd;
    --footer-text: #6a6a6a;
    --white: #ffffff;
  }
  * { margin: 0; padding: 0; box-sizing: border-box; }
  html, body { width: 1200px; height: 1087px; overflow: hidden; background: var(--white); }
  body { position: relative; font-family: "Arimo", Arial, sans-serif; color: var(--ink); }

  .site-header { position: absolute; top: 0; left: 0; width: 1200px; height: 88px; background: var(--white); z-index: 3; }
  .brand { position: absolute; left: 82px; top: 30px; display: flex; align-items: center; gap: 8px;
    font-family: "Lilita One", sans-serif; font-size: 20px; color: var(--brand-red); }
  .brand-dot { width: 22px; height: 22px; border-radius: 50%; background: var(--brand-red); }
  .main-nav { position: absolute; left: 423px; top: 31px; display: flex; align-items: center;
    font-family: "Lilita One", sans-serif; font-size: 22px; letter-spacing: 0.5px; }
  .main-nav a { text-decoration: none; color: var(--sky-blue); }
  .main-nav a.is-current { color: var(--ink); }
  .nav-star { width: 9px; height: 9px; margin: 0 20px; fill: var(--ink); }

  .btn-buy { position: absolute; display: flex; align-items: center; justify-content: center; gap: 12px;
    background: var(--brand-red); color: var(--white); text-decoration: none; border-radius: 4px;
    font-family: "Lilita One", sans-serif; box-shadow: 0 4px 0 var(--brand-red-dark); }
  .btn-buy svg { fill: none; stroke: var(--white); stroke-linecap: round; stroke-linejoin: round; }
  .btn-buy--header { left: 994px; top: 28px; width: 117px; height: 32px; font-size: 22px; }
  .btn-buy--header svg { width: 12px; height: 16px; stroke-width: 3.5; }
  .btn-buy--content { left: 86px; top: 834px; width: 190px; height: 52px; font-size: 38px; border-radius: 6px; }
  .btn-buy--content svg { width: 18px; height: 26px; stroke-width: 5; }

  .hero { position: absolute; top: 88px; left: 0; width: 1200px; height: 440px; overflow: hidden;
    background: linear-gradient(180deg, #56b1dc 0%, #8fd0ea 62%, #a6d86a 78%, #6fb42e 100%); }
  .nav-notch { position: absolute; left: 437px; top: 76px; width: 0; height: 0; z-index: 4;
    border-left: 16px solid transparent; border-right: 16px solid transparent; border-bottom: 12px solid #56b1dc; }
  .hero-burst { position: absolute; left: 88px; top: 0; width: 568px; height: 212px; border-radius: 28px;
    background: linear-gradient(110deg, rgba(255,255,255,0.55) 0%, rgba(255,255,255,0.4) 55%, rgba(227,65,151,0.45) 100%); }
  .hero-bike { position: absolute; left: 650px; top: 95px; width: 505px; height: 330px; border-radius: 60px 60px 120px 120px;
    background: linear-gradient(160deg, #f26a5e 0%, #eb1f27 55%, #b81a20 100%); }
  .hero-title { position: absolute; left: 205px; top: 230px; font-family: "Lilita One", sans-serif;
    font-size: 57px; line-height: 62px; color: var(--white); letter-spacing: 1px; font-weight: 400; }
  .hero-subtitle { position: absolute; left: 207px; top: 292px; font-family: "Alfa Slab One", serif;
    font-size: 33px; line-height: 44px; color: var(--ink); letter-spacing: 1px; }
  .hero-subtitle .star { font-size: 20px; vertical-align: 8px; }

  .hero-rule { position: absolute; top: 528px; left: 0; width: 1200px; height: 6px; background: #ececec; }

  .ribbon { position: absolute; top: 512px; left: 37px; width: 774px; height: 64px; z-index: 2; }
  .ribbon-tail { position: absolute; top: 24px; width: 41px; height: 40px; background: var(--gold-dark); }
  .ribbon-tail--left { left: 0; clip-path: polygon(0 0, 100% 0, 100% 100%, 0 100%, 28% 50%); }
  .ribbon-tail--right { right: 0; clip-path: polygon(0 0, 100% 0, 72% 50%, 100% 100%, 0 100%); }
  .ribbon-band { position: absolute; left: 30px; top: 0; width: 714px; height: 52px;
    background: linear-gradient(90deg, var(--gold) 0%, #e6ad00 60%, var(--gold-dark) 100%);
    font-family: "Lilita One", sans-serif; font-size: 37px; line-height: 54px; color: var(--white);
    padding-left: 19px; letter-spacing: 1px; font-weight: 400; }

  .intro { position: absolute; left: 86px; top: 594px; width: 425px; font-size: 17px; line-height: 26px; }
  .intro p { margin-bottom: 10px; }
  .intro .lead { font-weight: 700; }
  .intro a { color: var(--sky-blue); text-decoration: none; }

  .video-player { position: absolute; left: 571px; top: 599px; width: 539px; height: 288px;
    background: var(--video-bg); display: flex; align-items: center; justify-content: center; }
  .video-player svg { width: 110px; height: 110px; }

  .site-footer { position: absolute; left: 0; top: 1022px; width: 1200px; height: 65px;
    background: var(--footer-bg); border-top: 4px solid var(--footer-line);
    text-align: center; font-size: 12.5px; line-height: 18px; color: var(--footer-text); padding-top: 14px; }
</style>
</head>
<body>
  <header class="site-header">
    <div class="brand"><span class="brand-dot"></span>Zippa Loop Trike</div>
    <nav class="main-nav">
      <a href="#" class="is-current">HOME</a>
      <svg class="nav-star" viewBox="0 0 10 10"><polygon points="5,0 6.2,3.6 10,3.8 7,6.1 8.1,10 5,7.7 1.9,10 3,6.1 0,3.8 3.8,3.6"/></svg>
      <a href="#">GALLERY</a>
      <svg class="nav-star" viewBox="0 0 10 10"><polygon points="5,0 6.2,3.6 10,3.8 7,6.1 8.1,10 5,7.7 1.9,10 3,6.1 0,3.8 3.8,3.6"/></svg>
      <a href="#">CONTACT</a>
    </nav>
    <a href="#" class="btn-buy btn-buy--header">BUY <svg viewBox="0 0 12 16"><polyline points="3,2 9,8 3,14"/></svg></a>
  </header>
  <span class="nav-notch"></span>

  <section class="hero" role="img" aria-label="Cartoon sky with clouds, green hills and a winding road">
    <div class="hero-burst" role="img" aria-label="Hand-lettered 'Awesome' in a comic burst with shooting stars"></div>
    <div class="hero-bike" role="img" aria-label="Rendering of the ride-on trike, side view"></div>
    <h1 class="hero-title">NEW COLORFUL</h1>
    <p class="hero-subtitle">ZIPPA LOOP <span class="star">★</span>TRIKE<span class="star">★</span></p>
  </section>
  <div class="hero-rule"></div>

  <div class="ribbon">
    <span class="ribbon-tail ribbon-tail--left"></span>
    <span class="ribbon-tail ribbon-tail--right"></span>
    <h2 class="ribbon-band">TRY A SAFE ADVENTURE!</h2>
  </div>

  <main>
    <article class="intro">
      <p class="lead">Vivamus sodales ac odio nec feugiat.</p>
      <p>Lorem ipsum dolor sit amet, consectetur adipiscing elit. Donec ornare metus at lorem lobortis, vitae scelerisque lorem sollicitudin. Phasellus euismod laoreet auctor.</p>
      <p>In auctor nisl vel metus <a href="#">vel nunc.</a> Vulputate tristique. Praesent sagittis sapien libero, quis euismod nisl egestas eget. Aliquam quis risus et ipsum.&nbsp; tempus venenatis sit amet.</p>
    </article>
    <a href="#" class="btn-buy btn-buy--content">BUY <svg viewBox="0 0 18 26"><polyline points="4,3 14,13 4,23"/></svg></a>

    <div class="video-player" role="img" aria-label="Video of the trike in play">
      <svg viewBox="0 0 110 110">
        <circle cx="55" cy="55" r="50" fill="none" stroke="var(--video-icon)" stroke-width="5"/>
        <polygon points="41,36 41,74 72,55" fill="var(--video-icon)" stroke="var(--video-icon)" stroke-width="4" stroke-linejoin="round"/>
      </svg>
    </div>
  </main>

  <footer class="site-footer">
    © 2013, Zippa Loop Trike<br>All Rights Reserved
  </footer>
</body>
</html>
```